Luggage and travel essentials company needs Letterhead design (including logo)

Brenmoor luggage is a travel retailer focussed on selling luggage and travel essentials.
We are a company that have a traditional approach to customer service and also embraces the latest technology, especially where it improves the customer experience.
I would like the design to have an airport hint (airport imagery and font preferred), I would also like the colour blue to feature heavily (see attached image for colour hint).
The final design should aim to give the customer confidence that we are dependable and reliable (no script fonts or crazy colours please) but also reflect that we are an innovative and technology focused company.
I would like the letterhead design to include a logo and text.
I am interested in letterhead text containing an embedded logo (much like the 'A' in Zyvanta's logo is also used separately) Note: this is optional.
The text of the letterhead should include the words "Brenmoor Luggage & Travel Essentials", and should include a space for the company phone number, email address, website address along with the company physical address.
Target Market(s)
Affluent Adults aged 25 years and above - Predominantly female
Industry/Entity Type
Airport

```html
<!DOCTYPE html>
<html lang="en">
<head>
<meta charset="utf-8">
<title>Brenmoor Luggage &amp; Travel Essentials – Letterhead</title>
<link href="https://fonts.googleapis.com/css2?family=Exo+2:wght@400;500&display=swap" rel="stylesheet">
<style>
  :root {
    --backdrop: #02263d;
    --paper: #ffffff;
    --brand-blue: #0aa6e6;
    --brand-blue-pale: #d7eef8;
    --ink: #3d3d3f;
    --ink-soft: #4a4a4c;
  }
  html, body {
    margin: 0;
    padding: 0;
    width: 1200px;
    height: 1000px;
    overflow: hidden;
    background: var(--backdrop);
  }
  .canvas {
    position: relative;
    width: 1200px;
    height: 1000px;
  }
  .letterhead {
    position: absolute;
    left: 275px;
    top: 38px;
    width: 652px;
    height: 925px;
    background: var(--paper);
    overflow: hidden;
    font-family: "Exo 2", sans-serif;
  }
  .brand {
    position: absolute;
    left: 38px;
    top: 38px;
    display: flex;
    align-items: flex-start;
    gap: 7px;
  }
  .brand-mark {
    width: 30px;
    height: 30px;
    margin-top: 3px;
    background: var(--brand-blue);
  }
  .brand-name {
    color: var(--ink);
    font-weight: 500;
    line-height: 1;
  }
  .brand-name .primary {
    display: block;
    font-size: 31px;
    letter-spacing: -0.3px;
  }
  .brand-name .secondary {
    display: block;
    font-size: 15px;
    margin-top: 1px;
    margin-left: 2px;
  }
  .swoosh {
    position: absolute;
    left: 0;
    top: 0;
    width: 652px;
    height: 140px;
  }
  .contact {
    position: absolute;
    right: 20px;
    top: 79px;
    text-align: right;
    color: var(--ink-soft);
    font-size: 12.5px;
    font-style: normal;
    line-height: 16.5px;
  }
  .contact p { margin: 0; }
  .contact .divider { margin: 0 8px; }
  .corner-accent {
    position: absolute;
    left: 362px;
    top: 682px;
    width: 320px;
    height: 300px;
    background: var(--brand-blue-pale);
    border-top-left-radius: 46px;
  }
</style>
</head>
<body>
  <div class="canvas">
    <section class="letterhead">
      <svg class="swoosh" viewBox="0 0 652 140" aria-hidden="true">
        <path d="M23 92 C120 112 230 116 320 96 S470 60 516 54" fill="none" stroke="var(--brand-blue)" stroke-width="2.2" stroke-linecap="round"/>
      </svg>

      <header class="brand">
        <span class="brand-mark"></span>
        <span class="brand-name">
          <span class="primary">Brenmoor Luggage</span>
          <span class="secondary">&amp; Travel Essentials</span>
        </span>
      </header>

      <address class="contact">
        <p>14, Mill Lane, Alderby, Kent. AB1 2CD</p>
        <p>tel.: 01234 xxxxxx</p>
        <p>info@brenmoorluggage.co.uk<span class="divider">|</span>www.brenmoorluggage.co.uk</p>
      </address>

      <div class="corner-accent" aria-hidden="true"></div>
    </section>
  </div>
</body>
</html>
```